Business Card Design Project

New business card design front and back for IT company that does network support and web design.
Calloway IT
Doug Calloway
Managing Director
PO Box 918 Brinsley VIC 3421
doug@callowayit.example
www.callowayit.example

Industry/Entity Type

Business

```html
<!DOCTYPE html>
<html lang="en">
<head>
<meta charset="utf-8">
<title>Calloway IT – Business Card, Front and Back</title>
<link rel="stylesheet" href="https://fonts.googleapis.com/css2?family=Mulish:wght@400;500;700;800&display=swap">
<style>
  :root {
    --backdrop: #3b3938;
    --brand-blue: #00a7d0;
    --brand-blue-deep: #0a8fb6;
    --brand-blue-light: #1cb4da;
    --band-black: #19191b;
    --ink: #1b1b1d;
    --paper: #ffffff;
    --paper-shade: #d9d9db;
  }
  * { box-sizing: border-box; margin: 0; padding: 0; }
  html, body {
    width: 1200px;
    height: 848px;
    overflow: hidden;
  }
  body {
    position: relative;
    background: var(--backdrop);
    font-family: "Mulish", "Helvetica Neue", Arial, sans-serif;
    color: var(--ink);
  }
  .card {
    position: absolute;
    width: 538px;
    height: 299px;
    overflow: hidden;
    box-shadow: 0 3px 10px rgba(0,0,0,0.45);
  }

  /* Contact side */
  .card--contact { left: 238px; top: 117px; background: var(--paper); }
  .contact__header {
    position: absolute; left: 0; top: 0; width: 100%; height: 99px;
    background: linear-gradient(160deg, var(--brand-blue-light) 0%, var(--brand-blue) 55%, var(--brand-blue-deep) 100%);
  }
  .contact__brand {
    position: absolute; left: 34px; top: 30px;
    font-size: 21px; font-weight: 800; color: var(--paper);
    letter-spacing: 0.2px;
  }
  .contact__name {
    position: absolute; left: 219px; top: 71px;
    font-size: 23px; font-weight: 500; letter-spacing: 0.6px; color: var(--ink);
  }
  .contact__title-band {
    position: absolute; left: 0; top: 99px; width: 100%; height: 34px;
    background: var(--band-black);
  }
  .contact__title {
    position: absolute; left: 219px; top: 6px;
    font-size: 16px; font-weight: 500; letter-spacing: 0.5px; color: var(--paper);
  }
  .contact__body {
    position: absolute; left: 0; top: 133px; width: 100%; height: 166px;
    background: radial-gradient(ellipse at 75% 60%, var(--paper) 45%, var(--paper-shade) 110%);
  }
  .contact__details {
    position: absolute; left: 219px; top: 16px;
    list-style: none;
    font-size: 16px; line-height: 21px; letter-spacing: 0.5px; color: var(--ink);
  }

  /* Brand side */
  .card--brand {
    left: 431px; top: 451px; width: 539px; height: 300px;
    background: radial-gradient(ellipse at 30% 70%, var(--brand-blue) 40%, var(--brand-blue-deep) 120%);
    text-align: center;
  }
  .brand__sheen {
    position: absolute; inset: 0;
  }
  .brand__name {
    position: absolute; left: 0; width: 100%; top: 144px;
    font-size: 30px; font-weight: 800; letter-spacing: 0.3px; color: var(--paper);
  }
  .brand__tagline {
    position: absolute; left: 0; width: 100%; top: 188px;
    font-size: 15px; font-weight: 500; letter-spacing: 0.9px; color: var(--ink);
  }
</style>
</head>
<body>
  <section class="card card--contact" aria-label="Business card, contact side">
    <div class="contact__header">
      <p class="contact__brand">Calloway IT</p>
      <h1 class="contact__name">Doug Calloway</h1>
    </div>
    <div class="contact__title-band">
      <p class="contact__title">Managing Director</p>
    </div>
    <div class="contact__body">
      <ul class="contact__details">
        <li>PO Box 918 Brinsley VIC 3421</li>
        <li>0400 555 012</li>
        <li>doug@callowayit.example</li>
        <li>www.callowayit.example</li>
      </ul>
    </div>
  </section>

  <section class="card card--brand" aria-label="Business card, brand side">
    <svg class="brand__sheen" width="539" height="300" viewBox="0 0 539 300" aria-hidden="true">
      <path d="M0 300 C 120 120, 330 20, 539 0 L 539 0 C 360 40, 160 150, 60 300 Z" fill="#ffffff" opacity="0.05"/>
    </svg>
    <h2 class="brand__name">CALLOWAY IT</h2>
    <p class="brand__tagline">IT SOLUTIONS FOR YOUR BUSINESS</p>
  </section>
</body>
</html>
```